We need a business card design for a Dubai based company .

We need a business card for a Dubai based company called "Marwaneq Smoking Requisites Trading LLC". We mainly import Flavoured Tobacco products and Charcoal which is used for smoking in a Hookah/Shisha and distribute to the wholesalers and retailers. Logo file is attached herewith.

```html
<!DOCTYPE html>
<html lang="en">
<head>
<meta charset="utf-8">
<title>Marwaneq Smoking Requisites Trading LLC – Business Card</title>
<link href="https://fonts.googleapis.com/css2?family=Michroma&family=Questrial&display=swap" rel="stylesheet">
<style>
  :root {
    --page: #e9e7e4;
    --card-white: #f7f7f7;
    --card-black: #141516;
    --ink: #1d1d1f;
    --red: #b3262a;
    --grey: #5d5e60;
    --white: #ffffff;
  }
  * { box-sizing: border-box; margin: 0; padding: 0; }
  html, body { width: 1200px; height: 960px; overflow: hidden; }
  body {
    background: var(--page);
    font-family: "Questrial", "Century Gothic", sans-serif;
    color: var(--ink);
    position: relative;
  }
  .card {
    position: absolute;
    left: 250px;
    width: 700px;
    height: 400px;
    border-radius: 4px;
    box-shadow: 0 12px 30px rgba(0,0,0,0.18);
    overflow: hidden;
  }
  .card--front { top: 50px; background: linear-gradient(135deg, #ffffff 0%, var(--card-white) 55%, #e6e6e6 100%); }
  .card--back { top: 510px; }

  .brand {
    position: absolute;
    display: flex;
    align-items: center;
    gap: 14px;
  }
  .brand__square {
    width: 18px; height: 18px;
    background: var(--red);
    flex: none;
  }
  .brand__name {
    font-family: "Michroma", sans-serif;
    font-weight: 400;
    text-transform: uppercase;
    letter-spacing: 0.06em;
    line-height: 1.5;
  }
  .card--front .brand { left: 48px; top: 44px; }
  .card--front .brand__name { font-size: 15px; color: var(--ink); }

  .contacts {
    position: absolute;
    left: 48px;
    top: 150px;
    list-style: none;
    font-size: 21px;
    line-height: 1.38;
  }
  .contacts li { display: flex; align-items: center; gap: 10px; }
  .contacts svg { width: 18px; height: 18px; flex: none; }
  .contacts .accent { color: var(--red); }
  .contacts .address { padding-left: 0; margin-top: 4px; }

  .person {
    position: absolute;
    right: 56px;
    bottom: 48px;
    text-align: right;
  }
  .person__name {
    font-family: "Michroma", sans-serif;
    font-size: 24px;
    color: var(--red);
    letter-spacing: 0.02em;
  }
  .person__role { font-size: 21px; color: var(--ink); margin-top: 2px; }

  .back__texture {
    position: absolute; inset: 0;
    background: radial-gradient(ellipse at 35% 30%, #2a2b2d 0%, var(--card-black) 60%, #0a0a0b 100%);
  }
  .card--back .brand {
    left: 50%; top: 50%;
    transform: translate(-50%, -50%);
  }
  .card--back .brand__name { font-size: 20px; color: var(--white); text-align: left; }
</style>
</head>
<body>

  <section class="card card--front" aria-label="Business card front">
    <div class="brand">
      <span class="brand__square"></span>
      <p class="brand__name">Marwaneq<br>Smoking Requisites Trading LLC</p>
    </div>

    <ul class="contacts">
      <li>
        <svg viewBox="0 0 24 24" aria-hidden="true"><path fill="#b3262a" d="M6.6 10.8a15.1 15.1 0 0 0 6.6 6.6l2.2-2.2a1 1 0 0 1 1-.25 11.4 11.4 0 0 0 3.6.57 1 1 0 0 1 1 1V20a1 1 0 0 1-1 1A17 17 0 0 1 3 4a1 1 0 0 1 1-1h3.5a1 1 0 0 1 1 1c0 1.25.2 2.45.57 3.57a1 1 0 0 1-.25 1z"/></svg>
        +971 4 555 0142
      </li>
      <li>
        <svg viewBox="0 0 24 24" aria-hidden="true"><rect x="6" y="2" width="12" height="20" rx="2" fill="none" stroke="#b3262a" stroke-width="2"/><circle cx="12" cy="18" r="1.2" fill="#b3262a"/></svg>
        +971 50 555 0187
      </li>
      <li>
        <svg viewBox="0 0 24 24" aria-hidden="true"><rect x="2" y="5" width="20" height="14" fill="#b3262a"/><path d="M2 5l10 8 10-8" fill="none" stroke="#fff" stroke-width="1.6"/></svg>
        karim@marwaneqtrading.com
      </li>
      <li>
        <svg viewBox="0 0 24 24" aria-hidden="true"><circle cx="12" cy="12" r="10" fill="#b3262a"/><path d="M2 12h20M12 2c3 3 3 17 0 20M12 2c-3 3-3 17 0 20" fill="none" stroke="#fff" stroke-width="1.4"/></svg>
        www.<span class="accent">marwaneqtrading</span>.com
      </li>
      <li class="address">0/00 Harbour Rd Al Qusais, 0000</li>
    </ul>

    <div class="person">
      <p class="person__name">Karim Haddad</p>
      <p class="person__role">Owner/ CEO</p>
    </div>
  </section>

  <section class="card card--back" aria-label="Business card back">
    <div class="back__texture" role="img" aria-label="Dark background with a faint grid of offset line panels"></div>
    <div class="brand">
      <span class="brand__square"></span>
      <p class="brand__name">Marwaneq<br>Smoking Requisites Trading LLC</p>
    </div>
  </section>

</body>
</html>
```